Tidewell Rapid Rinse Web Design

We are looking for a web design that highlights our state of the art fully automated commercial vehicle washing equipment. Similar system to a car wash however this system is meant for the largest vehicles on our roadways. Transport trucks with or without a trailer, busses both highway and school, RV's from 5th wheel type to A Class. Cement trucks, dump trucks, vac trucks, fuel trucks etc. Pick ups with utility trailers...Refrigerator truck clean outs.
Tidewell Rapid Rinse will wash your vehicle quickly and with a minimal impact on the environment

Home page
About us
Why Tidewell
Services and pricing
Videos of wash system
Fleets
contact us

Target Market(s)

Commercial vehicle owners and operators as well as corporate fleets. Includes busses, municipal, school and highway.both school and

Industry/Entity Type

transportation

Coding

Coded - Design and coding required

Number of Pages Required

5+ page

Font styles to use
Sans Serif

Colors
0054AA
0677BA
7BADD7
CADEEF
E8F1F8

Requirements
Must have
• Welcome page,why us page which describes the financial and environmental benefits. payment processing page, contact us page, Services which is washing vehicles and greasing for commercial vehicles that want that service and grease
Nice to have
• pictures of both clean and dirty commercial vehicles ie. before and after

```html
<!DOCTYPE html>
<html lang="en">
<head>
<meta charset="utf-8">
<title>Tidewell Rapid Rinse</title>
<link href="https://fonts.googleapis.com/css2?family=Unbounded:wght@700;800;900&family=Inter:wght@400;500;600&display=swap" rel="stylesheet">
<style>
:root{
  --blue:#0054AA;
  --blue-mid:#0677BA;
  --blue-light:#7BADD7;
  --blue-pale:#CADEEF;
  --blue-mist:#E8F1F8;
  --ink:#111;
  --grey-bg:#f6f6f6;
  --white:#fff;
  --black:#000;
}
*{margin:0;padding:0;box-sizing:border-box}
html,body{width:1200px;height:4075px;overflow:hidden}
body{font-family:"Inter",Arial,sans-serif;color:var(--ink);background:var(--white);position:relative}
.display{font-family:"Unbounded","Arial Black",sans-serif;font-weight:800;text-transform:uppercase;letter-spacing:.02em}
.abs{position:absolute}

/* header */
.site-header{position:absolute;top:0;left:0;width:1200px;height:81px;background:var(--white)}
.logo{position:absolute;left:110px;top:16px}
.logo-name{font-family:"Unbounded",sans-serif;font-weight:800;font-size:24px;letter-spacing:.03em;color:var(--ink)}
.logo-sub{font-family:"Unbounded",sans-serif;font-weight:800;font-size:12px;letter-spacing:.62em;color:var(--blue);margin-top:2px}
.nav{position:absolute;top:30px;left:0;font-size:13px}
.nav span{position:absolute;white-space:nowrap}

/* hero */
.hero{position:absolute;top:81px;left:0;width:1200px;height:600px;
  background:linear-gradient(90deg,#4b4d52 0%,#8a8c90 35%,#b9bcc0 60%,#dfe2e5 85%,#cfd3d6 100%)}
.hero-title{position:absolute;left:110px;color:var(--white)}
.hero .t1{top:162px;font-size:34px}
.hero .t2{top:210px;font-size:62px;line-height:76px}
.btn{position:absolute;display:flex;align-items:center;justify-content:center;font-family:"Unbounded",sans-serif;font-weight:800;text-transform:uppercase;letter-spacing:.06em;border-radius:4px}
.btn-blue{background:var(--blue);color:var(--white)}
.btn-white{background:var(--white);color:var(--blue)}

/* mission */
.mission{position:absolute;top:681px;left:0;width:1200px;height:671px;background:var(--blue);color:var(--white)}
.mission h2{position:absolute;left:108px;top:70px;font-size:34px}
.mission-copy{position:absolute;left:653px;top:134px;width:440px;font-size:15px;line-height:26px}
.mission-copy p{margin-bottom:25px}

/* gallery */
.gallery h2{position:absolute;top:1432px;width:1200px;text-align:center;font-size:34px}
.tile{position:absolute;border-radius:8px;display:flex;align-items:center;justify-content:center;color:var(--white);font-family:"Unbounded",sans-serif;font-weight:800;font-size:20px;letter-spacing:.05em}
.dot{position:absolute;width:20px;height:20px;border-radius:50%;display:flex;align-items:center;justify-content:center}

/* services */
.services{position:absolute;top:2103px;left:0;width:1200px;height:664px;background:var(--grey-bg)}
.services h2{position:absolute;left:110px;top:96px;font-size:34px}
.svc{position:absolute;border-radius:8px;color:var(--white);font-family:"Unbounded",sans-serif;font-weight:800;font-size:15px;letter-spacing:.05em;line-height:21px}
.svc-card{position:absolute;background:var(--white);border-radius:8px;box-shadow:0 4px 20px rgba(0,0,0,.1)}

/* testimonials */
.members h2{position:absolute;top:2850px;width:1200px;text-align:center;font-size:34px}
.review{position:absolute;top:2952px;width:563px;height:218px;background:var(--white);border-radius:6px;box-shadow:0 2px 14px rgba(0,0,0,.07)}
.avatar{position:absolute;left:22px;top:20px;width:52px;height:52px;border-radius:50%;background:linear-gradient(135deg,#c9a98a,#5b4b3f)}
.review .name{position:absolute;left:96px;top:28px;font-size:16px}
.review .date{position:absolute;left:97px;top:52px;font-size:12px;color:#888}
.review .text{position:absolute;left:97px;top:78px;width:450px;font-size:12px;line-height:26px;color:#333;white-space:nowrap;overflow:hidden}
.review .stars{position:absolute;left:97px;top:160px;display:flex;gap:3px}

/* contact band */
.footer{position:absolute;top:3494px;left:0;width:1200px;height:581px;background:var(--black);color:var(--white)}
.contact-card{position:absolute;left:114px;top:3352px;width:976px;height:278px;border-radius:22px;background:linear-gradient(180deg,var(--blue-mid),#0a6fb3);color:var(--white);text-align:center}
.contact-card h2{padding-top:46px;font-size:34px}
.contact-card p{margin:22px auto 0;width:700px;font-size:15px;line-height:24px;color:var(--blue-mist)}

.f-col{position:absolute;top:243px}
.f-col h4{font-family:"Unbounded",sans-serif;font-weight:800;font-size:14px;letter-spacing:.05em;text-transform:uppercase;padding-bottom:14px;position:relative;white-space:nowrap}
.f-col h4::after{content:"";position:absolute;left:0;bottom:0;width:40px;height:1px;background:#555}
.f-col ul{list-style:none;font-size:14px}
.f-col li{display:flex;align-items:center;gap:10px;height:30px;white-space:nowrap}
.field{width:243px;border-bottom:1px solid #666;font-size:14px;color:#bbb;padding:18px 2px 8px}
</style>
</head>
<body>

<header class="site-header">
  <div class="logo">
    <div class="logo-name">TIDEWELL</div>
    <div class="logo-sub">RAPID RINSE</div>
  </div>
  <nav class="nav">
    <span style="left:561px">Home</span>
    <span style="left:636px">About Us</span>
    <span style="left:731px">Why Tidewell</span>
    <span style="left:888px">Services</span>
    <span style="left:978px">Pricing</span>
    <span style="left:1059px">More</span>
  </nav>
</header>

<section class="hero" role="img" aria-label="Photo of a truck inside an automated wash bay">
  <div class="hero-title display t1">Welcome to</div>
  <div class="hero-title display t2">Tidewell<br>Rapid Rinse</div>
  <div class="btn btn-blue" style="left:110px;top:374px;width:208px;height:52px;font-size:15px">Book a Wash</div>
  <div class="btn btn-blue" style="left:333px;top:374px;width:199px;height:52px;font-size:15px">Learn More</div>
  <div class="btn btn-white" style="left:540px;top:374px;width:190px;height:52px;font-size:15px">Contact Us</div>
</section>

<section class="mission">
  <h2 class="display">Mission Statement</h2>
  <svg class="abs" style="left:125px;top:124px" width="436" height="476" viewBox="0 0 436 476" role="img" aria-label="Photo of a blue truck in a hexagon frame">
    <defs><linearGradient id="hexFill" x1="0" y1="0" x2="1" y2="1"><stop offset="0" stop-color="#dfe4ea"/><stop offset=".5" stop-color="#2a62b5"/><stop offset="1" stop-color="#6c6f76"/></linearGradient></defs>
    <polygon points="218,0 436,119 436,357 218,476 0,357 0,119" fill="url(#hexFill)"/>
  </svg>
  <div class="mission-copy">
    <p>Lorem ipsum dolor sit amet, consectetur adipiscing elit, sed do eiusmod tempor incididunt ut labore et dolore magna aliqua. Quis ipsum suspendisse ultrices gravida. Risus commodo viverra maecenas accumsan lacus vel facilisis.</p>
    <p>Lorem ipsum dolor sit amet, consectetur adipiscing elit, sed do eiusmod tempor incididunt ut labore et dolore magna aliqua. Quis ipsum suspendisse ultrices gravida. Risus commodo viverra maecenas accumsan lacus vel facilisis.</p>
    <p>Lorem ipsum dolor sit amet, consectetur adipiscing elit, sed do eiusmod tempor incididunt ut labore et dolore magna aliqua. Quis ipsum suspendisse ultrices gravida. Risus commodo viverra maecenas accumsan lacus vel facilisis.</p>
  </div>
  <div class="btn btn-white" style="left:650px;top:517px;width:220px;height:55px;font-size:16px">Learn More</div>
</section>

<section class="gallery">
  <h2 class="display">Our Gallery</h2>
  <div class="tile" style="left:111px;top:1527px;width:256px;height:207px;background:linear-gradient(160deg,#9aa3ab,#7c6a55)" role="img" aria-label="Dirty cement mixer truck">Before</div>
  <div class="tile" style="left:379px;top:1527px;width:317px;height:424px;background:linear-gradient(180deg,#6f7f92,#b49a70 45%,#4d4a45)" role="img" aria-label="Dirty tipper truck on a dusty road">Before</div>
  <div class="tile" style="left:707px;top:1527px;width:381px;height:207px;background:linear-gradient(180deg,#6e7885,#c7cbd0 50%,#3a3c40)" role="img" aria-label="Clean white truck at a depot">After</div>
  <div class="tile" style="left:111px;top:1745px;width:256px;height:206px;background:linear-gradient(160deg,#8fb2d6,#cfd6dc 50%,#3e6d99)" role="img" aria-label="Clean cement mixer truck">After</div>
  <div class="tile" style="left:707px;top:1745px;width:158px;height:206px;background:linear-gradient(180deg,#a07a4b,#d07b1e 55%,#5a4630)" role="img" aria-label="Muddy orange dump truck">Before</div>
  <div class="tile" style="left:874px;top:1745px;width:214px;height:206px;background:linear-gradient(180deg,#c4c7cb,#5c6066 60%,#3a3c40)" role="img" aria-label="Clean grey dump truck">After</div>
  <div class="dot" style="left:576px;top:1997px;background:var(--blue)"><svg width="8" height="8" viewBox="0 0 8 8"><path d="M5 1 2 4l3 3" stroke="#fff" stroke-width="1.4" fill="none"/></svg></div>
  <div class="dot" style="left:604px;top:1997px;background:#e6e6e6"><svg width="8" height="8" viewBox="0 0 8 8"><path d="M3 1l3 3-3 3" stroke="#777" stroke-width="1.4" fill="none"/></svg></div>
</section>

<section class="services">
  <h2 class="display">Our Services</h2>
  <div class="svc" style="left:110px;top:193px;width:288px;height:357px;background:linear-gradient(180deg,#6a5a4c,#9c9a95 50%,#2e2f33)" role="img" aria-label="Truck passing through an automated wash">
    <div class="abs" style="left:27px;top:298px">AUTOMATED<br>TRUCK WASH</div>
  </div>
  <div class="svc-card" style="left:443px;top:181px;width:312px;height:381px">
    <div class="abs" role="img" aria-label="Worker washing a white truck in the bay" style="left:11px;top:12px;width:290px;height:206px;border-radius:8px;background:linear-gradient(90deg,#2c2f33,#9ea3a8 55%,#e2e5e8)"></div>
    <div class="abs display" style="left:22px;top:238px;font-size:15px;color:var(--ink);white-space:nowrap">Additional Services</div>
    <div class="abs" style="left:22px;top:262px;width:270px;font-size:12px;line-height:21px;color:#444">Lorem ipsum dolor sit amet, consectetur adipiscing elit, sed do eiusmod tempor incididunt ut labore et dolore magna aliqua.</div>
    <div class="abs" style="left:26px;top:330px;font-family:'Unbounded',sans-serif;font-weight:800;font-size:11px;letter-spacing:.05em;color:var(--blue);display:flex;align-items:center;gap:5px">LEARN MORE <svg width="11" height="11" viewBox="0 0 11 11"><circle cx="5.5" cy="5.5" r="5.5" fill="#0054AA"/><path d="M4.5 3l2.5 2.5L4.5 8" stroke="#fff" stroke-width="1.3" fill="none"/></svg></div>
  </div>
  <div class="svc" style="left:800px;top:193px;width:288px;height:357px;background:linear-gradient(180deg,#9aa3ad,#c98a3a 45%,#2d6f78 70%,#2a2c30)" role="img" aria-label="Row of parked fleet trucks">
    <div class="abs" style="left:20px;top:316px">FLEET SERVICES</div>
  </div>
</section>

<section class="members">
  <h2 class="display">What Our Members Say</h2>
  <div class="review" style="left:100px">
    <div class="avatar" role="img" aria-label="Member portrait"></div>
    <div class="name display">Morgan Ellery</div>
    <div class="date">2024-02-27</div>
    <div class="text">Lorem ipsum dolor sit amet, consectetur adipiscing elit, sed do eiusmod<br>tempor incididunt ut labore et dolore magna aliqua. Quis ipsum suspendisse<br>ultrices gravida. Risus commodo viverra maecenas accumsan lacus vel</div>
    <div class="stars"><svg width="76" height="12" viewBox="0 0 76 12" fill="#f4b400"><g id="st"><polygon points="6,0 7.6,4 12,4.3 8.6,7 9.7,11.5 6,9 2.3,11.5 3.4,7 0,4.3 4.4,4"/></g><use href="#st" x="16"/><use href="#st" x="32"/><use href="#st" x="48"/><use href="#st" x="64"/></svg></div>
  </div>
  <div class="review" style="left:725px">
    <div class="avatar" role="img" aria-label="Member portrait"></div>
    <div class="name display">Morgan Ellery</div>
    <div class="date">2024-02-27</div>
    <div class="text" style="width:470px">Lorem ipsum dolor sit amet, consectetur adipiscing elit, sed do eiusmod<br>tempor incididunt ut labore et dolore magna aliqua. Quis ipsum suspendisse<br>ultrices gravida. Risus commodo viverra maecenas accumsan lacus vel</div>
    <div class="stars"><svg width="76" height="12" viewBox="0 0 76 12" fill="#f4b400"><use href="#st"/><use href="#st" x="16"/><use href="#st" x="32"/><use href="#st" x="48"/><use href="#st" x="64"/></svg></div>
  </div>
  <div class="abs" style="left:276px;top:3249px;width:649px;height:3px;background:#ececec"></div>
  <div class="abs" style="left:430px;top:3248px;width:88px;height:5px;border-radius:3px;background:var(--blue)"></div>
</section>

<footer class="footer">
  <div class="f-col" style="left:113px">
    <h4>Contact</h4>
    <ul style="margin-top:18px">
      <li style="align-items:flex-start;height:auto;line-height:26px"><svg width="10" height="13" viewBox="0 0 10 13" style="margin-top:6px"><path d="M5 0a5 5 0 0 1 5 5c0 3.5-5 8-5 8S0 8.5 0 5a5 5 0 0 1 5-5z" fill="#1f7be0"/><circle cx="5" cy="5" r="1.8" fill="#000"/></svg>Lorem ipsum dolor<br>sit amet</li>
      <li style="margin-top:4px"><svg width="12" height="12" viewBox="0 0 12 12"><path d="M2.5 0.5l2 2.5-1.2 1.5a7 7 0 0 0 4.2 4.2L9 7.5l2.5 2-1 2C5 11.5 0.5 7 0.5 1.5z" fill="#1f7be0"/></svg>+1 888 555 0142</li>
      <li style="margin-top:8px"><svg width="13" height="10" viewBox="0 0 13 10"><rect width="13" height="10" rx="1" fill="#1f7be0"/><path d="M0.5 1l6 4.5 6-4.5" stroke="#000" stroke-width="1.2" fill="none"/></svg>hello@tidewellrapidrinse.com</li>
    </ul>
  </div>
  <div class="f-col" style="left:456px">
    <h4>Help Link</h4>
    <ul style="margin-top:14px">
      <li>› Terms &amp; Condtions</li>
      <li>› Privacy Policy</li>
      <li>› About Us</li>
      <li>› Support</li>
    </ul>
  </div>
  <div class="f-col" style="left:683px">
    <h4>Follow Us</h4>
    <ul style="margin-top:12px">
      <li><svg width="8" height="8"><circle cx="4" cy="4" r="4" fill="#fff"/></svg>Community</li>
      <li><svg width="8" height="8"><circle cx="4" cy="4" r="4" fill="#fff"/></svg>Photo Feed</li>
      <li><svg width="8" height="8"><circle cx="4" cy="4" r="4" fill="#fff"/></svg>News Feed</li>
      <li><svg width="8" height="8"><circle cx="4" cy="4" r="4" fill="#fff"/></svg>Short Clips</li>
    </ul>
  </div>
  <div class="f-col" style="left:844px">
    <h4>Newsletter Updates</h4>
    <div class="field" style="margin-left:2px">Name*</div>
    <div class="field" style="margin-left:2px">Email*</div>
    <div class="btn btn-blue" style="left:2px;top:170px;width:145px;height:38px;border-radius:20px;font-size:11px">Submit Now</div>
  </div>
  <div class="abs" style="left:113px;top:486px;width:976px;height:1px;background:#333"></div>
  <div class="abs" style="top:519px;width:1200px;text-align:center;font-size:14px">©Copyrights 2024&nbsp; Tidewell Rapid Rinse.&nbsp; |&nbsp;&nbsp; All Rights Reserved</div>
</footer>

<div class="contact-card">
  <h2 class="display">Contact Us</h2>
  <p>Lorem ipsum dolor sit amet, consectetur adipiscing elit, sed do eiusmod tempor incididunt ut labore et dolore magna aliqua. Quis ipsum suspendisse ultrices gravida. Risus commodo viverra maecenas accumsan lacus vel facilisis.</p>
  <div class="btn btn-blue" style="left:393px;top:194px;width:184px;height:43px;font-size:13px">Contact Us</div>
</div>

</body>
</html>
```